Steadfast MD - Sleep Medicine Specialist - Business Cards

We are a new medical practice called Steadfast MD. We are sleep medicine specialists and we will be conducting sleep studies on patients with sleep related ailments. We want the business card to be bold, professional, and clean with the logo as the stand out visual piece. We dont like wild flashy designs. We want our design to be bold and classic while at the same time conveying who we are and what we do. We are reliable, professional, and the best in the business.

Industry/Entity Type

Health Care

Contact Information for Business Card

- Clean
- Bold
- Classic
- not cluttered

Requirements
Must have
• logo, website, phone number
Nice to have
• several options to choose from
Should not have
• flashy imaged - reflective print - images of people sleeping

```html
<!DOCTYPE html>
<html lang="en">
<head>
<meta charset="utf-8">
<title>Steadfast MD – Business Card</title>
<link rel="stylesheet" href="https://fonts.googleapis.com/css2?family=Roboto:wght@400;500;700&display=swap">
<style>
  :root {
    --backdrop: #2b2b2b;
    --card-white: #fafafa;
    --brand-red: #e81c24;
    --ink: #141414;
    --body-ink: #1e1e1e;
    --faint-red: #fbe4e4;
    --paper: #ffffff;
  }
  * { margin: 0; padding: 0; box-sizing: border-box; }
  html, body {
    width: 1200px; height: 969px; overflow: hidden;
    background: var(--backdrop);
    font-family: "Roboto", Arial, sans-serif;
  }
  .canvas { position: relative; width: 1200px; height: 969px; }
  .card {
    position: absolute; left: 295px; width: 615px; height: 351px;
    border-radius: 18px; overflow: hidden;
  }
  .card-front { top: 90px; background: var(--card-white); }
  .card-back { top: 529px; background: var(--brand-red); }

  .backdrop-ring {
    position: absolute; left: 310px; top: -50px;
    width: 356px; height: 356px; border-radius: 50%;
    border: 17px solid var(--faint-red);
  }

  .brand { position: absolute; display: flex; align-items: center; }
  .brand-dot { border-radius: 50%; flex: none; }
  .brand-name { font-weight: 700; letter-spacing: -1px; white-space: nowrap; }

  .card-front .brand { left: 27px; top: 59px; gap: 10px; }
  .card-front .brand-dot { width: 60px; height: 60px; border: 4px solid var(--brand-red); }
  .card-front .brand-name { font-size: 32px; color: var(--ink); }

  .holder { position: absolute; left: 27px; top: 190px; }
  .holder-name { font-size: 21px; font-weight: 700; line-height: 1.1; color: var(--ink); }
  .holder-name .first { color: var(--brand-red); }
  .holder-role { font-size: 13.5px; font-weight: 500; color: var(--body-ink); margin-top: 1px; }

  .contacts { position: absolute; left: 27px; top: 250px; list-style: none; }
  .contacts li {
    display: flex; align-items: center; gap: 8px;
    height: 20.5px; font-size: 14px; color: var(--body-ink);
  }
  .contacts svg { width: 12px; height: 12px; flex: none; fill: var(--brand-red); }

  .divider {
    position: absolute; left: 240px; top: 298px;
    width: 1.5px; height: 27px; background: var(--brand-red);
  }
  .address {
    position: absolute; left: 256px; top: 293px;
    font-size: 14px; line-height: 17.5px; color: var(--body-ink);
  }

  .card-back .brand { left: 109px; top: 126px; gap: 8px; }
  .card-back .brand-dot { width: 101px; height: 101px; border: 5px solid var(--paper); }
  .card-back .brand-name { font-size: 48px; color: var(--paper); }
</style>
</head>
<body>
<main class="canvas">
  <section class="card card-front" aria-label="Business card front">
    <div class="backdrop-ring" aria-hidden="true"></div>

    <div class="brand">
      <span class="brand-dot" aria-hidden="true"></span>
      <span class="brand-name">Steadfast MD</span>
    </div>

    <div class="holder">
      <p class="holder-name"><span class="first">DANIEL</span> HAYES</p>
      <p class="holder-role">Manager</p>
    </div>

    <ul class="contacts">
      <li>
        <svg viewBox="0 0 24 24" aria-hidden="true"><path d="M6.6 10.8a15.1 15.1 0 0 0 6.6 6.6l2.2-2.2a1 1 0 0 1 1-.25 11.4 11.4 0 0 0 3.6.57 1 1 0 0 1 1 1V20a1 1 0 0 1-1 1A17 17 0 0 1 3 4a1 1 0 0 1 1-1h3.5a1 1 0 0 1 1 1c0 1.25.2 2.45.57 3.57a1 1 0 0 1-.25 1z"/></svg>
        (555) 4170 - 2386
      </li>
      <li>
        <svg viewBox="0 0 24 24" aria-hidden="true"><path d="M7 1h10a2 2 0 0 1 2 2v18a2 2 0 0 1-2 2H7a2 2 0 0 1-2-2V3a2 2 0 0 1 2-2zm0 3v14h10V4zm5 15.5a1 1 0 1 0 0 2 1 1 0 0 0 0-2z"/></svg>
        (555) 7382 - 1049
      </li>
      <li>
        <svg viewBox="0 0 24 24" aria-hidden="true"><path d="M2 5h20v14H2zm2 2v.4l8 5.2 8-5.2V7l-8 5.1z"/></svg>
        info@steadfastmd.com
      </li>
      <li>
        <svg viewBox="0 0 24 24" aria-hidden="true"><path d="M12 2a10 10 0 1 0 0 20 10 10 0 0 0 0-20zm-1 17.9A8 8 0 0 1 4.1 10.9L9 15.8v1a2 2 0 0 0 2 2zm6.9-2.5A2 2 0 0 0 16 16h-1v-3a1 1 0 0 0-1-1H8v-2h2a1 1 0 0 0 1-1V7h2a2 2 0 0 0 2-2v-.4a8 8 0 0 1 2.9 12.8z"/></svg>
        www.steadfastmd.com
      </li>
    </ul>

    <span class="divider" aria-hidden="true"></span>
    <address class="address" style="font-style: normal;">
      214 N. Harbor Ave.<br>
      Country name , MN 40817
    </address>
  </section>

  <section class="card card-back" aria-label="Business card back">
    <div class="brand">
      <span class="brand-dot" aria-hidden="true"></span>
      <span class="brand-name">Steadfast MD</span>
    </div>
  </section>
</main>
</body>
</html>
```